Business Card Design for Kidvale (Hires out childrens play areas)

Looking to have a business card designed for a company we just bought. The company rents out childrens play areas.

I have uploaded a couple of examples of the kind of business card style I like. Here are two more examples:

https://quorvastudio.nz/project/bright-romp-branding/
https://imgvaultcdn.com/design_img/8841052/302917/302917_5518203_8841052_b73e19a2_image.jpg

I think a white card will be best due to all the colours in the logo.

Size we require: 3.75" x 2.25" (horizontally orientated) with a 0.125" bleed

Uploaded is two versions of our logo.

Details for the card:
1. My name: Liam Verster
2. Title: Managing Director
3. Phone no: 021 563 417
4. Email: liam@kidvale.co.nz
5. URL: www.kidvale.co.nz
6. Address:
PO Box 318625
Fernlea, Auckland

Let me know if you need anything else.

Target Market(s)

Hospitals, doctors surgeries, bed shops, etc.

Contact Information for Business Card

Details for the card:
1. My name: Liam Verster
3. Phone no: 021 563 417
5. URL: www.kidvale.co.nz
6. Address:
PO Box 318625
Fernlea, Auckland

Requirements
Should not have
• Not too busy.

```html
<!DOCTYPE html>
<html lang="en">
<head>
<meta charset="utf-8">
<title>Kidvale Business Card</title>
<link href="https://fonts.googleapis.com/css2?family=Open+Sans:wght@400;600;700&display=swap" rel="stylesheet">
<style>
  :root {
    --stage: #e9e7e4;
    --navy: #243a98;
    --glow: #1f9de3;
    --ink: #1f4f9e;
    --band: #1a5bb5;
    --icon: #e5433a;
    --accent: #f7941d;
    --paper: #ffffff;
  }
  * { margin: 0; padding: 0; box-sizing: border-box; }
  html, body { width: 1200px; height: 676px; overflow: hidden; }
  body {
    background: var(--stage);
    font-family: "Open Sans", Arial, sans-serif;
    position: relative;
  }
  .card {
    position: absolute;
    top: 173px;
    width: 550px;
    height: 330px;
    border-radius: 3px;
    box-shadow: 0 6px 18px rgba(0,0,0,0.18);
    overflow: hidden;
  }
  .card-front {
    left: 35px;
    background: radial-gradient(ellipse 55% 60% at 50% 50%, var(--glow) 0%, #2b6fc9 45%, var(--navy) 100%);
    display: flex; align-items: center; justify-content: center;
  }
  .card-back { left: 615px; background: var(--paper); }
  .brand {
    display: flex; align-items: center; gap: 12px;
    font-weight: 700; letter-spacing: 0.5px;
  }
  .brand-dot { border-radius: 50%; background: var(--accent); flex: none; }
  .card-front .brand { font-size: 58px; color: var(--paper); }
  .card-front .brand-dot { width: 30px; height: 30px; }
  .card-back .brand {
    position: absolute; left: 42px; top: 138px;
    font-size: 44px; color: var(--ink);
  }
  .card-back .brand-dot { width: 22px; height: 22px; }
  .divider {
    position: absolute; left: 292px; top: 34px; width: 2px; height: 262px;
    background: linear-gradient(to bottom, rgba(26,91,181,0), var(--band) 50%, rgba(26,91,181,0));
  }
  .edge-band {
    position: absolute; right: 0; top: 0; width: 30px; height: 100%;
    background: var(--band);
  }
  .contact { position: absolute; left: 318px; top: 64px; color: var(--ink); }
  .contact-name { font-size: 17px; font-weight: 700; line-height: 1.2; }
  .contact-title { font-size: 12.5px; margin: 2px 0 0 14px; }
  .contact-list { list-style: none; margin: 26px 0 0 28px; font-size: 12.5px; line-height: 1.35; }
  .contact-list li { display: flex; align-items: flex-start; gap: 8px; margin-bottom: 3px; }
  .contact-list svg { flex: none; width: 11px; height: 11px; margin-top: 3px; }
</style>
</head>
<body>
  <section class="card card-front" aria-label="Card front">
    <div class="brand"><span class="brand-dot"></span>Kidvale</div>
  </section>

  <section class="card card-back" aria-label="Card back">
    <div class="brand"><span class="brand-dot"></span>Kidvale</div>
    <div class="divider"></div>
    <div class="contact">
      <p class="contact-name">Liam Verster</p>
      <p class="contact-title">Managing Director</p>
      <ul class="contact-list">
        <li>
          <svg viewBox="0 0 12 12" aria-hidden="true"><circle cx="6" cy="6" r="6" fill="var(--icon)"/><path d="M4 3.2l1 1.3-.6.7c.4.8 1 1.4 1.8 1.8l.7-.6 1.3 1-.6.9C5.6 8.2 3.8 6.4 3.1 4.4z" fill="#fff"/></svg>
          <span>021 563 417</span>
        </li>
        <li>
          <svg viewBox="0 0 12 12" aria-hidden="true"><circle cx="6" cy="6" r="6" fill="var(--icon)"/><rect x="3" y="4" width="6" height="4" fill="#fff"/><path d="M3 4l3 2.2L9 4" stroke="var(--icon)" stroke-width=".7" fill="none"/></svg>
          <span>liam@kidvale.co.nz</span>
        </li>
        <li>
          <svg viewBox="0 0 12 12" aria-hidden="true"><circle cx="6" cy="6" r="6" fill="var(--icon)"/><circle cx="6" cy="6" r="2.8" fill="none" stroke="#fff" stroke-width=".8"/><path d="M3.2 6h5.6M6 3.2v5.6" stroke="#fff" stroke-width=".6"/></svg>
          <span>www.kidvale.co.nz</span>
        </li>
        <li>
          <svg viewBox="0 0 12 12" aria-hidden="true"><circle cx="6" cy="6" r="6" fill="var(--icon)"/><path d="M6 9.2C4.6 7.6 4 6.6 4 5.4a2 2 0 0 1 4 0c0 1.2-.6 2.2-2 3.8z" fill="#fff"/><circle cx="6" cy="5.3" r=".7" fill="var(--icon)"/></svg>
          <span>PO Box 318625<br>Fernlea, Auckland</span>
        </li>
      </ul>
    </div>
    <div class="edge-band"></div>
  </section>
</body>
</html>
```